Glass repair Packaging Design Project

The product is a glass scratch repair kit inside a clear, plastic clamshell pack.
Two covers need to be designed: one for the front and one for the back of the clamshell pack, both 150mm(height) x 145mm(width).

The scratch repair kit comes in 2 sizes: 2" repair pads and 3" repair pads. Each size kit comes in 3 grades: light scratch removal, medium scratch removal and deep scratch removal.

The main packaging will stay the same for every kit but needs an area on the front cover to say size and grade e.g

2" repair pad, light scratch repair
or
3" repair pad, deep scratch repair

The kit is for the DIY market and so "DIY" needs to be on the front cover quite prominently.
"Drill required but not included" to be on back cover.

Repairable damage includes:
Scuffs
Scratches
Water marks
Acid marks
Wiper blade marks

(front cover)
Glass types suitable for repair include:
patio doors
window units
glass shower screens
glass tables
glass fish tanks
automotive glass
marine glass
domestic glass

The back cover of the pack needs to say the kit contents

This kit contains:
instructions
micro fibre cloth
dust mask
abrasive discs
50ml polishing compound
polishing pads
spray bottle
backing pad for drill

On the bottom of the back cover
www.panevellastore.co.uk

Industry/Entity Type

Automotive

Requirements
Must have
• The colour scheme must work with the logo colours. The logo is black and green.

```html
<!DOCTYPE html>
<html lang="en">
<head>
<meta charset="utf-8">
<title>Panevella Scratch Repair Kit – Pack Covers</title>
<link rel="stylesheet" href="https://fonts.googleapis.com/css2?family=Alfa+Slab+One&family=PT+Sans:wght@400;700&family=PT+Sans+Narrow:wght@700&display=swap">
<style>
  :root {
    --backdrop: #5f6357;
    --lime-bright: #b0da22;
    --lime-mid: #98c61c;
    --lime-deep: #77a917;
    --frame-green: #5c8a10;
    --badge-red: #d8121b;
    --ink: #000000;
    --paper: #ffffff;
  }
  * { margin: 0; padding: 0; box-sizing: border-box; }
  html, body { width: 1170px; height: 1200px; overflow: hidden; background: var(--backdrop); }
  .sheet { position: relative; width: 1170px; height: 1200px; }

  .cover {
    position: absolute;
    width: 546px;
    height: 565px;
    overflow: hidden;
    color: var(--paper);
    font-family: "PT Sans", sans-serif;
  }
  .cover--front { left: 24px; background: linear-gradient(150deg, var(--lime-bright) 0%, var(--lime-mid) 45%, var(--lime-deep) 100%); }
  .cover--back  { left: 595px; background: linear-gradient(150deg, var(--lime-deep) 0%, var(--lime-mid) 50%, var(--lime-bright) 100%); }
  .row-top { top: 20px; }
  .row-bottom { top: 611px; }

  .size-badge { position: absolute; left: 0; top: 0; width: 120px; height: 120px; }

  .brand-frame {
    position: absolute;
    left: 206px; top: 25px;
    width: 330px; height: 110px;
    border: 6px solid var(--frame-green);
    box-shadow: 0 0 6px var(--frame-green), inset 0 0 6px var(--frame-green);
    display: flex; align-items: center; justify-content: center;
  }
  .brand-name {
    font-family: "PT Sans", sans-serif;
    font-weight: 700;
    font-size: 44px;
    color: var(--ink);
    letter-spacing: -0.5px;
  }

  .section-title {
    position: absolute;
    font-family: "Alfa Slab One", serif;
    font-weight: 400;
    color: var(--paper);
  }
  .glass-types .section-title { left: 11px; top: 199px; font-size: 13px; letter-spacing: 0.3px; }
  .glass-list {
    position: absolute; left: 13px; top: 233px;
    list-style: none; font-size: 13px; line-height: 17.6px;
  }
  .glass-list li::before, .contents-list li::before { content: "· "; }

  .diy-mark {
    position: absolute; left: 12px; top: 498px;
    font-family: "Alfa Slab One", serif;
    font-size: 44px; color: var(--ink); letter-spacing: 1px;
  }
  .grade-label {
    position: absolute; left: 226px; top: 527px;
    font-family: "Alfa Slab One", serif;
    font-size: 21px; color: var(--paper); letter-spacing: 0.6px;
  }

  .kit-contents .section-title { left: 36px; top: 29px; font-size: 19px; letter-spacing: 0.5px; }
  .contents-list {
    position: absolute; left: 36px; top: 68px;
    list-style: none; font-size: 19.5px; line-height: 25.5px;
  }

  .pack-footer {
    position: absolute; left: 0; right: 0; top: 496px;
    text-align: center; padding-left: 14px;
  }
  .drill-note { font-weight: 700; font-size: 12px; }
  .shop-url {
    font-family: "PT Sans Narrow", sans-serif;
    font-weight: 700; font-size: 24px; margin-top: 5px;
  }
</style>
</head>
<body>
<main class="sheet">

  <!-- 3" deep grade -->
  <section class="cover cover--front row-top">
    <svg class="size-badge" viewBox="0 0 120 120" aria-hidden="true">
      <path d="M110 0 A110 110 0 0 1 0 90 L0 46 A62 62 0 0 0 64 0 Z" fill="var(--badge-red)"/>
      <text x="54" y="54" transform="rotate(-40 54 54)" text-anchor="middle" font-family="Alfa Slab One, serif" font-size="30" fill="#fff">3"</text>
    </svg>
    <div class="brand-frame"><span class="brand-name">panevella</span></div>
    <div class="glass-types">
      <h2 class="section-title">Glass types suitable for repair</h2>
      <ul class="glass-list">
        <li>Patio doors</li><li>Windows units</li><li>Glass shower screens</li><li>Glass tables</li>
        <li>Glass fish tanks</li><li>Automotive glass</li><li>Marine glass</li><li>Domestic glass</li>
      </ul>
    </div>
    <div class="diy-mark">DIY</div>
    <div class="grade-label">Deep Scratch Repair</div>
  </section>

  <section class="cover cover--back row-top">
    <div class="kit-contents">
      <h2 class="section-title">This Kit Contains</h2>
      <ul class="contents-list">
        <li>Instructions</li><li>Micro fibre cloth</li><li>Dust mask</li><li>Abrasive disks</li>
        <li>50ml Polishing Compound</li><li>Polishing pads</li><li>Spray bottle</li><li>Backing pad for drill</li>
      </ul>
    </div>
    <footer class="pack-footer">
      <p class="drill-note">Drill requiered but not included!</p>
      <p class="shop-url">www.panevellastore.co.uk</p>
    </footer>
  </section>

  <!-- 2" light grade -->
  <section class="cover cover--front row-bottom">
    <svg class="size-badge" viewBox="0 0 120 120" aria-hidden="true">
      <path d="M110 0 A110 110 0 0 1 0 90 L0 46 A62 62 0 0 0 64 0 Z" fill="var(--badge-red)"/>
      <text x="54" y="54" transform="rotate(-40 54 54)" text-anchor="middle" font-family="Alfa Slab One, serif" font-size="30" fill="#fff">2"</text>
    </svg>
    <div class="brand-frame"><span class="brand-name">panevella</span></div>
    <div class="glass-types">
      <h2 class="section-title">Glass types suitable for repair</h2>
      <ul class="glass-list">
        <li>Patio doors</li><li>Windows units</li><li>Glass shower screens</li><li>Glass tables</li>
        <li>Glass fish tanks</li><li>Automotive glass</li><li>Marine glass</li><li>Domestic glass</li>
      </ul>
    </div>
    <div class="diy-mark">DIY</div>
    <div class="grade-label">Light Scratch Repair</div>
  </section>

  <section class="cover cover--back row-bottom">
    <div class="kit-contents">
      <h2 class="section-title">This Kit Contains</h2>
      <ul class="contents-list">
        <li>Instructions</li><li>Micro fibre cloth</li><li>Dust mask</li><li>Abrasive disks</li>
        <li>50ml Polishing Compound</li><li>Polishing pads</li><li>Spray bottle</li><li>Backing pad for drill</li>
      </ul>
    </div>
    <footer class="pack-footer">
      <p class="drill-note">Drill requiered but not included!</p>
      <p class="shop-url">www.panevellastore.co.uk</p>
    </footer>
  </section>

</main>
</body>
</html>
```